Business Card Design

I need a business card for my company i am starting. I will be providing stump grinding services. I use a motorized machine to grind stumps down under the ground so that they are out of the way and out of sight. I'm looking for my card to have maroon or dark red somewhere in the card to match my truck. I'm going to use this card to advertise and also serve as a design to wrap my truck tailgate as advertisement so i want it to match. the dark maroon color of my truck. I wouldn't mind using bright colors or color for the rest of the card or the lettering or any designs on the card. In the images i have provided i like how there are saw blades integrated into these people advertisements. I also like the illustration of the stump grinder. I also provided a picture of the actual cutting wheel or blade of the grinder.

Industry/Entity Type

Business

Contact Information for Business Card

Company Name - Oakline Stump Grinding
Phone - 407-219-5573
Email - harlow.stumpwork@quillpost.net
Name and title - Thomas Harlow - Owner and operator
Company Slogan - You find them, I'll grind them

```html
<!DOCTYPE html>
<html lang="en">
<head>
<meta charset="utf-8">
<title>Oakline Stump Grinding – Business Card</title>
<link href="https://fonts.googleapis.com/css2?family=Open+Sans:wght@400;600;800&display=swap" rel="stylesheet">
<style>
  :root {
    --stage: #e9e4dc;
    --card-white: #ffffff;
    --orange: #e7740f;
    --orange-dark: #d4620a;
    --red: #d3172a;
    --maroon: #7a1d18;
    --ink: #1a1a1a;
    --photo-light: #a98f6f;
    --photo-dark: #5a4532;
  }
  html, body {
    margin: 0;
    width: 1200px;
    height: 892px;
    overflow: hidden;
    background: var(--stage);
    font-family: "Open Sans", sans-serif;
  }
  .card {
    position: absolute;
    left: 100px;
    top: 156px;
    width: 1000px;
    height: 580px;
    border-radius: 30px;
    overflow: hidden;
    background: var(--card-white);
    box-shadow: 0 14px 36px rgba(0,0,0,0.25);
  }
  .card-shapes {
    position: absolute;
    inset: 0;
  }
  .brand {
    position: absolute;
    left: 250px;
    top: 70px;
    display: flex;
    align-items: center;
    gap: 18px;
  }
  .brand-dot {
    width: 58px;
    height: 58px;
    border-radius: 50%;
    background: var(--maroon);
  }
  .brand-name {
    font-weight: 800;
    font-size: 44px;
    color: var(--maroon);
    line-height: 1;
    letter-spacing: -0.5px;
  }
  .slogan {
    position: absolute;
    left: 330px;
    top: 150px;
    font-size: 28px;
    color: var(--ink);
  }
  .contact {
    position: absolute;
    right: 50px;
    top: 250px;
    text-align: right;
    color: #fff;
  }
  .contact-name {
    font-size: 42px;
    font-weight: 400;
    margin: 0;
    line-height: 1.1;
  }
  .contact-title {
    font-size: 25px;
    margin: 2px 0 44px;
    opacity: 0.95;
  }
  .contact-line {
    display: flex;
    justify-content: flex-end;
    align-items: center;
    gap: 16px;
    font-size: 26px;
    margin-bottom: 12px;
  }
  .icon {
    width: 26px;
    height: 26px;
    background: #fff;
    border-radius: 4px;
    display: flex;
    align-items: center;
    justify-content: center;
  }
</style>
</head>
<body>
  <div class="card">
    <svg class="card-shapes" width="1000" height="580" viewBox="0 0 1000 580">
      <defs>
        <linearGradient id="photoTone" x1="0" y1="0" x2="1" y2="1">
          <stop offset="0" stop-color="var(--photo-light)"/>
          <stop offset="1" stop-color="var(--photo-dark)"/>
        </linearGradient>
        <linearGradient id="orangeTone" x1="0" y1="0" x2="1" y2="1">
          <stop offset="0" stop-color="var(--orange)"/>
          <stop offset="1" stop-color="var(--orange-dark)"/>
        </linearGradient>
      </defs>
      <rect class="orange-panel" x="380" y="225" width="620" height="355" fill="url(#orangeTone)"/>
      <path class="photo-area" role="img" aria-label="Photo of a stump grinder cutting wheel in soil"
            d="M0 200 Q330 160 520 580 L0 580 Z" fill="url(#photoTone)"/>
      <path class="red-arc" d="M0 200 Q330 160 520 580" fill="none" stroke="var(--red)" stroke-width="14"/>
    </svg>

    <div class="brand">
      <span class="brand-dot"></span>
      <span class="brand-name">Oakline Stump Grinding</span>
    </div>
    <div class="slogan">You find them, I'll grind them</div>

    <div class="contact">
      <p class="contact-name">Thomas Harlow</p>
      <p class="contact-title">Owner and operator</p>
      <div class="contact-line">
        <span>407-219-5573</span>
        <span class="icon">
          <svg width="18" height="18" viewBox="0 0 24 24"><path fill="#e7740f" d="M6.6 10.8a15 15 0 0 0 6.6 6.6l2.2-2.2c.3-.3.7-.4 1-.2 1.1.4 2.3.6 3.6.6.6 0 1 .4 1 1V20c0 .6-.4 1-1 1A17 17 0 0 1 3 4c0-.6.4-1 1-1h3.5c.6 0 1 .4 1 1 0 1.3.2 2.5.6 3.6.1.3 0 .7-.2 1z"/></svg>
        </span>
      </div>
      <div class="contact-line">
        <span>harlow.stumpwork@quillpost.net</span>
        <span class="icon">
          <svg width="18" height="18" viewBox="0 0 24 24"><rect x="2" y="5" width="20" height="14" rx="2" fill="#e7740f"/><path d="M3 6l9 7 9-7" fill="none" stroke="#fff" stroke-width="2"/></svg>
        </span>
      </div>
    </div>
  </div>
</body>
</html>
```